Vehicle Wrap - Kestrel CX 300 (2014)

We have a brand new white 2014 Kestrel CX 300 Van that we want logo'd. We are looking for a partial wrap to full wrap. We want the sides and back designed for sure. If design can be accomplished with partical design, this is a plus but not a requirement.

We want a "catchy" colorful head turning BOLD design. We dont want a busy design. We do want something BOLD and clean and easily recognisable. We want our brand to STAND OUT.

The wrap should include the following on all sides (if room):
* Our large "hc" circular logo (this can be ENLARGED & stand alone)
* Business Name "Harbor Crafters"
* Phone Number 209-555-0173
* Web Address www.hcvox.com
* What we specialize in: IT Consulting - Networks - Voice - Data
* Locations Serviced: Modesto - Stockton - Pleasanton - Fresno

Color scheme: Our logo blue, black, white, touch of an accent color if needed. We want bold, but nothing too busy. Simplicity, neat design and unique look and feel are important.

We only have one vehicle so far, so this vehicle wrap needs to "POP" and stand out in a crowd of cars. :) !!

** See attached business card for design ideas

Target Market(s)

Businesses - All Sizes - Needing IT Support

Font styles to use
Sans Serif

Colors
0555a3
3176b5
33a6d7
85cae6
0592cd
abd036
f68e4e
f37022
9bcb3c

Requirements
Must have
• Large Logo, clean design, BOLD, colorful, yet simple.
• Company Name: Harbor Crafters
• Circle Logo
• Phone #: 209-555-0173 (HCVX)
• Website: www.hcvox.com
• Services: IT Consulting - Networks - Voice - Data
• Partical to Full Wrap (prefer partical - less expensive)
Nice to have
• BIG BOLD - simple and clean. Dont like a busy design which has text of all sizes scattered everywhere. Fonts need to be easy to read, clean and sleek. We want to stand out - be recognized. We would like to see our logo LARGE (whether the entire logo or just the hc circle part - either is okay. Our locations and services would be nice to display on the bottom rather than in the middle somewhere.
• Some kind of watermark or vector style image would be good. We dont want the van really plain and simple. Bold & Colorful - yet clean and professional are more in lines with what we want.
Should not have
• Too Busy, too messy, lots of text, text of different sizing and styles. (We like consistancy!) :)
• If anything is on a slant or tilted, it needs to go with the flow of the angle of the van.

```html
<!DOCTYPE html>
<html lang="en">
<head>
<meta charset="utf-8">
<title>Harbor Crafters – Rear Door Wrap Options</title>
<link href="https://fonts.googleapis.com/css2?family=Roboto+Condensed:wght@700&family=Open+Sans:wght@600&display=swap" rel="stylesheet">
<style>
  :root {
    --brand-blue: #2375be;
    --brand-sky: #85cae6;
    --panel-white: #f2f1ec;
    --panel-edge: #d9d8d2;
    --badge-grey: #5a5a5a;
    --page-bg: #ffffff;
  }
  * { box-sizing: border-box; margin: 0; padding: 0; }
  html, body {
    width: 1200px; height: 1000px; overflow: hidden;
    background: var(--page-bg);
  }
  .sheet { position: relative; width: 1200px; height: 1000px; }

  .option-number {
    position: absolute; width: 62px; height: 62px; border-radius: 50%;
    background: var(--badge-grey); color: #fff;
    font: 700 38px/62px "Open Sans", sans-serif; text-align: center;
  }

  .door-panel {
    position: absolute; width: 270px; height: 250px;
    background: var(--panel-white); border: 1px solid var(--panel-edge);
    border-radius: 16px 16px 6px 6px; overflow: hidden;
  }
  .rear-window {
    position: absolute; left: 12px; top: 14px; width: 246px; height: 86px;
    border-radius: 8px 8px 14px 14px;
  }
  .rear-window.is-blue { background: var(--brand-blue); }
  .rear-window.is-sky { background: var(--brand-sky); }

  .company-name {
    position: absolute; left: 0; right: 0; top: 20px; text-align: center;
    font: 700 24px/1 "Roboto Condensed", sans-serif; letter-spacing: 0.5px;
    color: var(--brand-blue);
  }
  .services {
    position: absolute; left: 0; right: 0; top: 68px; text-align: center;
    font: 700 9.5px/1 "Roboto Condensed", sans-serif; text-transform: uppercase;
    color: var(--brand-blue); word-spacing: 1px;
  }
  .services .dot {
    display: inline-block; width: 5px; height: 5px; border-radius: 50%;
    background: currentColor; margin: 0 5px; vertical-align: 1px;
  }
  .is-blue .company-name { color: #fff; }
  .is-blue .services.light { color: #fff; }
  .is-blue .services.sky { color: var(--brand-sky); }

  .hc-circle {
    position: absolute; left: 2px; top: 152px; width: 130px; height: 130px;
    border-radius: 50%; background: var(--brand-blue);
  }
  .hc-circle span {
    position: absolute; left: 16px; top: 16px;
    font: 700 58px/1 "Roboto Condensed", sans-serif; color: var(--panel-white);
  }

  .web, .phone {
    position: absolute; right: 30px; color: var(--brand-blue);
    font-family: "Open Sans", sans-serif; font-weight: 600;
  }
  .web { font-size: 13px; }
  .phone {
    font-family: "Roboto Condensed", sans-serif; font-weight: 700; font-size: 15px;
    display: flex; align-items: center; gap: 2px;
  }
  .phone svg { width: 13px; height: 13px; }
  .contact-split .web { top: 131px; }
  .contact-split .phone { top: 220px; }
  .contact-stacked .web { top: 210px; right: 24px; font-size: 12px; }
  .contact-stacked .phone { top: 226px; right: 24px; }
</style>
</head>
<body>
<main class="sheet">

  <div class="option-number" style="left:216px;top:34px">1</div>
  <div class="option-number" style="left:584px;top:34px">2</div>
  <div class="option-number" style="left:956px;top:34px">3</div>
  <div class="option-number" style="left:216px;top:517px">4</div>
  <div class="option-number" style="left:584px;top:517px">5</div>
  <div class="option-number" style="left:956px;top:517px">6</div>

  <!-- Option 1 -->
  <section class="door-panel contact-split" style="left:112px;top:152px">
    <div class="rear-window">
      <p class="company-name">Harbor Crafters</p>
      <p class="services">IT Consulting<i class="dot"></i>Networks<i class="dot"></i>Voice<i class="dot"></i>Data</p>
    </div>
    <div class="hc-circle"><span>hc</span></div>
    <p class="web">www.hcvox.com</p>
    <p class="phone"><svg viewBox="0 0 16 16"><circle cx="8" cy="8" r="7" fill="none" stroke="currentColor" stroke-width="1.6"/><path d="M5.5 4.5l1.5 0.3 0.5 1.8-1 0.8a5 5 0 0 0 2.1 2.1l0.8-1 1.8 0.5 0.3 1.5c-0.5 0.6-1.4 0.8-2.3 0.5a7 7 0 0 1-4.2-4.2c-0.3-0.9-0.1-1.8 0.5-2.3z" fill="currentColor"/></svg>209-555-0173</p>
  </section>

  <!-- Option 2 -->
  <section class="door-panel contact-split" style="left:480px;top:152px">
    <div class="rear-window is-blue">
      <p class="company-name">Harbor Crafters</p>
      <p class="services light">IT Consulting<i class="dot"></i>Networks<i class="dot"></i>Voice<i class="dot"></i>Data</p>
    </div>
    <div class="hc-circle"><span>hc</span></div>
    <p class="web">www.hcvox.com</p>
    <p class="phone"><svg viewBox="0 0 16 16"><circle cx="8" cy="8" r="7" fill="none" stroke="currentColor" stroke-width="1.6"/><path d="M5.5 4.5l1.5 0.3 0.5 1.8-1 0.8a5 5 0 0 0 2.1 2.1l0.8-1 1.8 0.5 0.3 1.5c-0.5 0.6-1.4 0.8-2.3 0.5a7 7 0 0 1-4.2-4.2c-0.3-0.9-0.1-1.8 0.5-2.3z" fill="currentColor"/></svg>209-555-0173</p>
  </section>

  <!-- Option 3 -->
  <section class="door-panel contact-stacked" style="left:852px;top:152px">
    <div class="rear-window is-blue">
      <p class="company-name">Harbor Crafters</p>
      <p class="services light">IT Consulting<i class="dot"></i>Networks<i class="dot"></i>Voice<i class="dot"></i>Data</p>
    </div>
    <div class="hc-circle"><span>hc</span></div>
    <p class="web">www.hcvox.com</p>
    <p class="phone"><svg viewBox="0 0 16 16"><circle cx="8" cy="8" r="7" fill="none" stroke="currentColor" stroke-width="1.6"/><path d="M5.5 4.5l1.5 0.3 0.5 1.8-1 0.8a5 5 0 0 0 2.1 2.1l0.8-1 1.8 0.5 0.3 1.5c-0.5 0.6-1.4 0.8-2.3 0.5a7 7 0 0 1-4.2-4.2c-0.3-0.9-0.1-1.8 0.5-2.3z" fill="currentColor"/></svg>209-555-0173</p>
  </section>

  <!-- Option 4 -->
  <section class="door-panel contact-split" style="left:112px;top:612px">
    <div class="rear-window is-blue">
      <p class="company-name">Harbor Crafters</p>
      <p class="services sky">IT Consulting<i class="dot"></i>Networks<i class="dot"></i>Voice<i class="dot"></i>Data</p>
    </div>
    <div class="hc-circle"><span>hc</span></div>
    <p class="web">www.hcvox.com</p>
    <p class="phone"><svg viewBox="0 0 16 16"><circle cx="8" cy="8" r="7" fill="none" stroke="currentColor" stroke-width="1.6"/><path d="M5.5 4.5l1.5 0.3 0.5 1.8-1 0.8a5 5 0 0 0 2.1 2.1l0.8-1 1.8 0.5 0.3 1.5c-0.5 0.6-1.4 0.8-2.3 0.5a7 7 0 0 1-4.2-4.2c-0.3-0.9-0.1-1.8 0.5-2.3z" fill="currentColor"/></svg>209-555-0173</p>
  </section>

  <!-- Option 5 -->
  <section class="door-panel contact-stacked" style="left:480px;top:612px">
    <div class="rear-window is-blue">
      <p class="company-name">Harbor Crafters</p>
      <p class="services sky">IT Consulting<i class="dot"></i>Networks<i class="dot"></i>Voice<i class="dot"></i>Data</p>
    </div>
    <div class="hc-circle"><span>hc</span></div>
    <p class="web">www.hcvox.com</p>
    <p class="phone"><svg viewBox="0 0 16 16"><circle cx="8" cy="8" r="7" fill="none" stroke="currentColor" stroke-width="1.6"/><path d="M5.5 4.5l1.5 0.3 0.5 1.8-1 0.8a5 5 0 0 0 2.1 2.1l0.8-1 1.8 0.5 0.3 1.5c-0.5 0.6-1.4 0.8-2.3 0.5a7 7 0 0 1-4.2-4.2c-0.3-0.9-0.1-1.8 0.5-2.3z" fill="currentColor"/></svg>209-555-0173</p>
  </section>

  <!-- Option 6 -->
  <section class="door-panel contact-stacked" style="left:852px;top:612px">
    <div class="rear-window is-sky">
      <p class="company-name">Harbor Crafters</p>
      <p class="services">IT Consulting<i class="dot"></i>Networks<i class="dot"></i>Voice<i class="dot"></i>Data</p>
    </div>
    <div class="hc-circle"><span>hc</span></div>
    <p class="web">www.hcvox.com</p>
    <p class="phone"><svg viewBox="0 0 16 16"><circle cx="8" cy="8" r="7" fill="none" stroke="currentColor" stroke-width="1.6"/><path d="M5.5 4.5l1.5 0.3 0.5 1.8-1 0.8a5 5 0 0 0 2.1 2.1l0.8-1 1.8 0.5 0.3 1.5c-0.5 0.6-1.4 0.8-2.3 0.5a7 7 0 0 1-4.2-4.2c-0.3-0.9-0.1-1.8 0.5-2.3z" fill="currentColor"/></svg>209-555-0173</p>
  </section>

</main>
</body>
</html>
```